Webdesign für KFZ-Service-Betrieb
Zielgruppe
Wartung, Reparatur und Instandsetzung von Kraftfahrzeugen aller Marken.
Reifenhandel, Old- und Youngtimer-Service, An- und Verkauf von Fahrzeugen.
Aufgabenstellung
Firmenfarbe ist blau.
Moderner, Übersichtlicher und Transparenter Auftritt erwünscht.

```html
<!DOCTYPE html>
<html lang="de">
<head>
<meta charset="utf-8">
<title>Der Schrauber – Autoservice nach Maß</title>
<link rel="stylesheet" href="https://fonts.googleapis.com/css2?family=Roboto:ital,wght@0,300;0,400;0,500;0,700;1,400&display=swap">
<style>
:root{
  --navy:#11142a;
  --navy-deep:#0c0e1f;
  --brand:#2e3192;
  --brand-soft:#8f91d6;
  --lavender:#e4e4f3;
  --lavender-line:#c9c9e6;
  --quote-mark:#b3b4df;
  --text:#2b2b33;
  --white:#ffffff;
  --map:#4f5580;
}
*{margin:0;padding:0;box-sizing:border-box}
html,body{width:1200px;height:2906px;overflow:hidden}
body{font-family:"Roboto",sans-serif;color:var(--text);background:var(--white);position:relative}
.abs{position:absolute}

/* hero */
.hero{position:absolute;left:0;top:0;width:1200px;height:600px;
  background:linear-gradient(90deg,#1a1d33 0%,#15182c 65%,#0d0f1f 66%,#0a0b18 100%);overflow:hidden}
.hero-wheel{position:absolute;left:560px;top:90px;width:530px;height:530px;border-radius:50%;
  background:radial-gradient(circle,rgba(80,85,140,.25) 0%,rgba(40,44,80,.15) 60%,rgba(0,0,0,0) 71%)}
.brand-name{position:absolute;left:232px;top:20px;font-weight:700;font-size:23px;color:var(--white);display:flex;align-items:center;gap:10px}
.brand-name .dot{width:30px;height:30px;border-radius:50%;background:var(--brand)}
.nav{position:absolute;top:31px;font-size:10px;color:var(--white);letter-spacing:.3px}
.hero-bar{position:absolute;left:226px;top:257px;width:4px;height:85px;background:var(--brand)}
.hero-title{position:absolute;left:245px;top:250px;font-size:43px;line-height:50px;font-weight:500;color:var(--white);
  background:linear-gradient(90deg,#fff 40%,#a9abe0 100%);-webkit-background-clip:text;background-clip:text;-webkit-text-fill-color:transparent}
.hero-sub{position:absolute;left:245px;top:356px;font-size:30px;font-weight:300;color:#3b3fb5}
.bar-footer{position:absolute;left:232px;font-size:7.5px;color:var(--white);display:flex;align-items:center;gap:8px}
.bar-footer i{display:inline-block;width:7px;height:7px;border-radius:50%;background:var(--white)}
.bar-copy{position:absolute;right:234px;font-size:7.5px;color:var(--white)}

/* offers + services */
.services-bg{position:absolute;left:0;top:600px;width:1200px;height:1092px}
.photo{position:absolute;background:linear-gradient(135deg,#c81d1d 0%,#b8b8bd 45%,#6d6f78 75%,#a39b8c 100%)}
.ghost{position:absolute;font-size:92px;font-weight:700;color:rgba(46,49,146,.06);letter-spacing:2px}
.offer-title{position:absolute;left:609px;top:726px;font-size:19px;line-height:25px;font-weight:500;color:var(--brand)}
.offer-title::before{content:"";position:absolute;left:-9px;top:2px;width:3px;height:46px;background:var(--brand)}
.offer-body{position:absolute;left:609px;top:798px;font-size:11px;line-height:17.5px;color:var(--text)}
.offer-body p{margin-bottom:17px}
.more{position:absolute;left:609px;top:950px;font-size:15px;color:var(--brand)}
.svc{position:absolute;left:234px;width:340px}
.svc h3{font-size:19px;font-weight:400;color:var(--brand);margin-bottom:13px}
.svc p{font-size:11px;line-height:17.5px}
.svc .arr{color:var(--brand);font-size:14px;margin-left:6px}
.svc.active::before{content:"";position:absolute;left:-8px;top:-2px;width:3px;height:37px;background:var(--brand)}
.dots{position:absolute;left:659px;top:1509px;display:flex;gap:9px}
.dots span{width:8px;height:8px;border-radius:50%;background:var(--white)}
.dots span:first-child{background:var(--brand)}

/* quote */
.quote{position:absolute;left:0;top:1692px;width:1200px;height:316px;background:linear-gradient(180deg,#121527 0%,#0c0e1e 100%)}
.quote-mark{position:absolute;left:296px;top:1740px;font-family:"Roboto",sans-serif;font-weight:700;font-size:300px;line-height:300px;color:var(--quote-mark)}
.quote-text{position:absolute;left:546px;top:1796px;width:430px;font-style:italic;font-size:15.5px;line-height:25px;color:var(--white)}
.quote-author{position:absolute;left:900px;top:1886px;width:66px;text-align:right;font-style:italic;font-weight:700;font-size:15px;color:var(--white)}

/* map + contact */
.map{position:absolute;left:0;top:2008px;width:1200px;height:413px;background:linear-gradient(135deg,#545a86 0%,#4a5079 50%,#555b88 100%)}
.contact-line{position:absolute;left:598px;top:2421px;width:2px;height:38px;background:var(--brand)}
.contact{position:absolute;left:0;top:2476px;width:1200px;text-align:center;font-size:15px;line-height:25px;color:var(--brand)}
.contact h4{font-weight:500;font-size:15px;margin-top:25px}
.contact-mark{position:absolute;left:565px;top:2733px;width:70px;height:70px;border-radius:50%;background:var(--brand)}
.site-footer{position:absolute;left:0;top:2863px;width:1200px;height:43px;background:var(--navy-deep)}
</style>
</head>
<body>

<header class="hero">
  <div class="hero-wheel" role="img" aria-label="Technische Zeichnung eines Autorads über dunklem Armaturenbrett"></div>
  <div class="brand-name"><span class="dot"></span>Der Schrauber</div>
  <nav>
    <span class="nav" style="left:536px">LEISTUNGEN</span>
    <span class="nav" style="left:651px">PHILOSOPHIE</span>
    <span class="nav" style="left:769px">FIRMENGESCHICHTE</span>
    <span class="nav" style="left:921px">KONTAKT</span>
  </nav>
  <div class="hero-bar"></div>
  <h1 class="hero-title">WARTUNG, REPARATUR<br>&amp; INSTANDSETZUNG</h1>
  <p class="hero-sub">von Kraftfahrzeugen aller Marken.</p>
  <div class="bar-footer" style="top:571px"><i></i><i></i><i></i><span>Autoservice nach Maß</span></div>
  <div class="bar-copy" style="top:571px">Der Schrauber © Copyright 2016</div>
</header>

<svg class="services-bg" viewBox="0 600 1200 1092" width="1200" height="1092">
  <polygon points="1200,688 1200,1692 0,1692 0,1562" fill="#e4e4f3"/>
  <circle cx="803" cy="1342" r="372" fill="none" stroke="#c9c9e6" stroke-width="1"/>
  <circle cx="803" cy="1342" r="335" fill="none" stroke="#d6d6ec" stroke-width="1"/>
  <circle cx="803" cy="1342" r="265" fill="none" stroke="#7a7dc6" stroke-width="1.3" stroke-dasharray="5 5"/>
  <g fill="#e4e4f3" stroke="#b9bbe2" stroke-width="1.3" font-family="Roboto,sans-serif" font-size="17" text-anchor="middle">
    <circle cx="656" cy="1132" r="15"/><circle cx="568" cy="1257" r="20" stroke-dasharray="3 3"/>
    <circle cx="570" cy="1439" r="15"/><circle cx="656" cy="1548" r="15"/>
  </g>
  <g fill="#b9bbe2" font-family="Roboto,sans-serif" font-size="17" text-anchor="middle">
    <text x="656" y="1138">1</text><text x="568" y="1263">2</text><text x="570" y="1445">3</text><text x="656" y="1554">4</text>
  </g>
</svg>

<div class="ghost" style="left:530px;top:680px">ANGEBOTE</div>
<div class="photo" style="left:0;top:663px;width:536px;height:319px" role="img" aria-label="Foto: Alufelge an einem roten Auto"></div>
<h2 class="offer-title">JETZT GÜNSTIGE SOMMERREIFEN/<br>SOMMERRÄDER KAUFEN!</h2>
<div class="offer-body">
  <p>Bei uns gibt es Markenreifen schon ab 39,- Euro<br>wir liefern alle Fabrikate zu günstigen Preisen.</p>
  <p>Fragen Sie nach Ihren individuellen Angebot.</p>
  <p>Montage-Preis <b>ab 9,50 Euro</b> (pro Rad)<br>Räderwechsel-Preise <b>12,90 / 14,90 / 19,90</b> pro Fahrzeug</p>
</div>
<a class="more">Mehr →</a>

<div class="ghost" style="left:200px;top:1108px">LEISTUNGEN</div>
<div class="svc" style="top:1153px"><h3>SERVICE</h3><p>Bei uns ist nicht nur Ihr Stellaris bestens „aufgehoben“, Wir bieten unsere Service-Leistungen für alle Marken an.<span class="arr">→</span></p></div>
<div class="svc active" style="top:1252px;width:360px"><h3>UNFALLINSTANDSETZUNG</h3><p>Wir arbeiten nach den vorgeschriebenen Standards der Hersteller.<span class="arr">→</span></p></div>
<div class="svc" style="top:1332px"><h3>VERKAUF</h3><p>Wir sind Ihr Ansprechpartner Nr. 1 für Gebrauchtfahrzeuge aller Hersteller - und ganz speziell für „Junge Gebrauchte“.<span class="arr">→</span></p></div>
<div class="svc" style="top:1433px"><h3>FAHRZEUGPFLEGE</h3><p>Waschanlage ist nicht gleich Waschanlage! Lackschonende und gründliche Reinigung ist mit unserer Textilfließwaschanlage gewährleistet.<span class="arr">→</span></p></div>
<div class="photo" style="left:658px;top:1179px;width:542px;height:320px;background:linear-gradient(135deg,#dfe3ea 0%,#2f4f8f 45%,#1d2f63 70%,#3a3a40 100%)" role="img" aria-label="Foto: Mechaniker wechselt ein Rad mit Schlagschrauber"></div>
<div class="dots"><span></span><span></span><span></span><span></span></div>

<section class="quote" role="img" aria-label="Dunkles Foto eines Autocockpits"></section>
<div class="quote-mark">“</div>
<p class="quote-text">Ich möchte mich noch einmal ausdrücklich für Ihre jahrelang erbrachten exzellenten Dienstleistungen bedanken und wünsche dem gesamten Team weiterhin alles Gute!</p>
<p class="quote-author">J.M.</p>

<div class="map" role="img" aria-label="Stadtplan von Berlin mit Standort der Werkstatt"></div>
<div class="contact-line"></div>
<address class="contact" style="font-style:normal">
  Lindenhofstraße 42<br>10115 Berlin
  <h4>ÖFFNUNGSZEITEN:</h4>
  Mo.-Fr.: 07.30 Uhr - 18.00 Uhr<br>
  Sa.: 09.00 Uhr-12.00 Uhr<br>
  Telefon:030/5550140<br>
  Telefax:030/5550149
</address>
<div class="contact-mark"></div>

<footer class="site-footer">
  <div class="bar-footer" style="top:18px"><i></i><i></i><i></i><span>Autoservice nach Maß</span></div>
  <div class="bar-copy" style="top:18px">Der Schrauber © Copyright 2016</div>
</footer>

</body>
</html>
```